TQR Habitat Stewards 2019

We need a 2 page flyer to advertise our upcoming program. The program covers 5 months May-September 2019 and is focused on conservation.I have attached some options that i like. It needs to be striking.

Text in newly uploaded document 'HSFlyer2'

Target Market(s)

Conservation
Conscious travelers
30-45 year olds
Environmental
Adventure/Hiking
Citizen Science

Font styles to use
Sans Serif

Colors
0355a3
fbed22

Requirements
Must have
• A travel conservation focus
• Highlight the significance of the 'in the world' status of the project
Nice to have
• A yellow border, making it look similar to the cover of Wanderfield Quarterly

```html
<!DOCTYPE html>
<html lang="en">
<head>
<meta charset="utf-8">
<title>TQR Habitat Stewards 2019 Flyer</title>
<link rel="stylesheet" href="https://fonts.googleapis.com/css2?family=Roboto+Condensed:wght@300;400;700&family=Cabin:wght@500&display=swap">
<style>
:root{
  --navy:#2d4a93;
  --blue:#1f5fae;
  --sky:#1b7bc3;
  --ink:#1d3557;
  --text:#555;
  --cream:#f6f1e2;
  --bg:#e4e4e4;
}
*{box-sizing:border-box;margin:0;padding:0}
html,body{width:1200px;height:1200px;overflow:hidden;background:var(--bg)}
body{position:relative;font-family:"Roboto Condensed",sans-serif}
.page{position:absolute;background:#fff;overflow:hidden}
.page-front{left:47px;top:258px;width:533px;height:689px}
.page-back{left:602px;top:258px;width:539px;height:697px}
.front-art{position:absolute;inset:0}
.brand{position:absolute;left:412px;top:82px;width:96px;height:60px;display:flex;align-items:center;justify-content:center;text-align:center;font-weight:700;font-size:13px;line-height:1.2;color:var(--blue)}
.front-copy{position:absolute;left:19px;top:278px;width:272px}
.front-title{font-weight:300;font-size:22px;line-height:26px;color:var(--navy);letter-spacing:.1px;margin-bottom:10px;white-space:nowrap}
.front-lead{font-size:10.2px;line-height:16px;color:var(--blue);text-transform:uppercase;text-align:justify;margin-bottom:6px}
.quote{font-size:10.5px;line-height:13px;color:var(--navy);margin-bottom:2px;white-space:nowrap}
.quote-by{font-size:9.8px;line-height:12px;color:var(--text);margin:0 0 8px 5px}
.body{font-size:10.2px;line-height:15.6px;color:var(--text);text-align:justify;margin-bottom:5px}
.front-footer{position:absolute;left:0;bottom:0;width:100%;height:39px;background:var(--navy);color:#fff;font-size:14px;letter-spacing:2.4px;line-height:39px;padding-left:24px;white-space:nowrap}
.hero{position:absolute;left:0;top:0;width:100%;height:349px;background:linear-gradient(180deg,#4a7fc4 0%,#8fc0e0 18%,#3fc6d8 38%,#66d9e3 55%,#e9efe0 78%,#f4efdf 100%)}
.hero-title{position:absolute;left:27px;top:225px;font-family:"Cabin",sans-serif;font-weight:500;font-size:47px;line-height:60px;color:var(--ink);letter-spacing:.5px}
.thumbs{position:absolute;top:349px;left:0;width:100%;height:84px;display:flex}
.thumb{flex:1;height:100%}
.cols{position:absolute;top:433px;left:0;width:100%;height:130px;display:flex}
.col{flex:1;padding:8px 6px 0 2px;color:#fff;overflow:hidden}
.col:nth-child(1){background:#1e73bd}.col:nth-child(2){background:#1a66ab;padding-left:10px}
.col:nth-child(3){background:#17599a;padding-left:10px}.col:nth-child(4){background:#134d88;padding-left:8px}
.col:nth-child(5){background:#0f4176;padding-left:6px}
.col h3{font-weight:300;font-size:11px;line-height:15px;text-transform:uppercase}
.col h3 b{font-weight:400;display:block}
.col p{font-size:5.6px;line-height:8px;margin-top:10px;text-align:justify}
.awards{position:absolute;top:568px;left:0;width:100%;height:36px;background:var(--sky);color:#fff;font-family:"Cabin",sans-serif;font-size:18px;line-height:36px;text-align:center;letter-spacing:.3px}
.partners{position:absolute;top:604px;left:0;width:100%;height:75px;background:var(--cream);display:flex;align-items:center;justify-content:space-around;padding:0 10px}
.partner{width:36px;height:28px;border-radius:4px}
.partner.round{border-radius:50%;width:40px;height:34px}
.back-footer{position:absolute;bottom:0;left:0;width:100%;height:18px;background:var(--blue)}
</style>
</head>
<body>
<section class="page page-front">
  <svg class="front-art" width="533" height="689" viewBox="0 0 533 689">
    <defs>
      <linearGradient id="sunset" x1="0" y1="0" x2="0" y2="1">
        <stop offset="0" stop-color="#9c4f8a"/><stop offset=".3" stop-color="#e07a9a"/>
        <stop offset=".6" stop-color="#6a4d86"/><stop offset="1" stop-color="#2b3560"/>
      </linearGradient>
      <linearGradient id="coast" x1="0" y1="0" x2="0" y2="1">
        <stop offset="0" stop-color="#c9dbe8"/><stop offset=".5" stop-color="#3a77a8"/><stop offset="1" stop-color="#4d6a3a"/>
      </linearGradient>
      <linearGradient id="reef" x1="0" y1="0" x2="1" y2="1">
        <stop offset="0" stop-color="#1f6ea0"/><stop offset=".5" stop-color="#2fa3b5"/><stop offset="1" stop-color="#3c5a2c"/>
      </linearGradient>
    </defs>
    <path role="img" aria-label="Photo of a wooden boat on a calm lagoon at sunset" d="M0,0H533V30C470,60 430,130 380,190C330,250 200,258 0,262Z" fill="url(#sunset)"/>
    <path d="M0,266C200,262 330,254 382,194C432,134 472,64 533,36" fill="none" stroke="var(--navy)" stroke-width="5"/>
    <polygon role="img" aria-label="Photo of a hiker on a coastal lookout" points="368,146 446,224 368,302 290,224" fill="url(#coast)"/>
    <polygon role="img" aria-label="Photo of turquoise reef water beside a forested ridge" points="533,180 533,470 388,325" fill="url(#reef)"/>
    <polygon points="358,318 396,356 358,394 320,356" fill="var(--navy)"/>
    <polygon role="img" aria-label="Photo of steep cliffs above a clear blue bay" points="428,370 545,487 428,604 311,487" fill="url(#reef)"/>
    <polygon points="358,572 396,610 358,648 320,610" fill="#1f73c4"/>
    <polygon points="533,510 533,650 395,650" fill="var(--navy)"/>
    <circle cx="460" cy="112" r="64" fill="#fff" stroke="var(--navy)" stroke-width="4"/>
    <circle cx="460" cy="112" r="56" fill="none" stroke="var(--navy)" stroke-width="1.5"/>
  </svg>
  <div class="brand">TQR Habitat Stewards</div>
  <div class="front-copy">
    <h1 class="front-title">MAKE A DIFFERENCE IN 2019</h1>
    <p class="front-lead">The best way to experience the true beauty of Tarqua Ridge Island is to see it for yourself; join our TQR Habitat Stewards program in 2019 and be involved in a world class, award winning holistic conservation effort – protecting paradise.</p>
    <p class="quote">“[Tarqua Ridge Island is] so extraordinary it is almost unbelievable”.</p>
    <p class="quote-by">Sir Edmund Rowley</p>
    <p class="body">Tarqua Ridge Island located 600km off the New South Wales coast is renowned for its spectacular scenery, important breeding grounds for colonies of seabirds, and its rich biodiversity including many endangered and critically endangered species not found anywhere else in the world.</p>
    <p class="body">TQR Habitat Stewards believe in protecting the island’s unique biodiversity while showcasing world class conservation in action. We are dedicated to empowering like-minded people to make a difference through robust citizen science, inspiring educational experiences, and tangible local conservation action.</p>
    <p class="body">Potential quote: Look deeper into nature and you will understand everything better.</p>
  </div>
  <div class="front-footer">FOR MORE DETAILS, VISIT : www.tarquaridgeisland.info</div>
</section>

<section class="page page-back">
  <div class="hero" role="img" aria-label="Aerial photo of a white sand spit curving through a turquoise lagoon"></div>
  <h2 class="hero-title">Enjoy Your<br>Holiday With Us!</h2>
  <div class="thumbs">
    <div class="thumb" role="img" aria-label="Photo of a seabird chick in its nest" style="background:linear-gradient(135deg,#8a8274,#4d4a42)"></div>
    <div class="thumb" role="img" aria-label="Photo of a snorkeller surveying the reef" style="background:linear-gradient(135deg,#2b8fc9,#0f4f8a)"></div>
    <div class="thumb" role="img" aria-label="Photo of a forested mountain peak" style="background:linear-gradient(180deg,#9bb4b0,#3f5a34)"></div>
    <div class="thumb" role="img" aria-label="Photo of volunteers sorting samples outdoors" style="background:linear-gradient(135deg,#7a8a5a,#4a5a3a)"></div>
    <div class="thumb" role="img" aria-label="Photo of a child holding a large insect" style="background:linear-gradient(135deg,#e8c4c8,#9a6a8a)"></div>
  </div>
  <div class="cols">
    <div class="col"><h3>Birds of Tarqua Ridge <b>Island – May 2019</b></h3><p>Showcasing the island's incredible bird species. Watch wild seabirds return from the sky at dusk and help our team record nesting and feeding of rare seabirds.</p></div>
    <div class="col"><h3>Tarqua Ridge Island's Marine Environment <b>June 2019</b></h3><p>Our seabirds are being harmed by ocean plastic. Help survey the island's reefs and shores, gather useful data on debris and work with experts on support solutions.</p></div>
    <div class="col"><h3>Invasive Species <b>July 2019</b></h3><p>Invasive weeds are among the most serious threats to the island's biodiversity and world heritage values. Hike to remote sites and help remove weeds with our experts.</p></div>
    <div class="col"><h3>Amazing Invertebrates <b>August 2019</b></h3><p>Rodents are voracious predators of invertebrates. Their loss would harm the island's natural balance. This month we celebrate the return of rare insects and snails across the island and the globe.</p></div>
    <div class="col"><h3>Protecting Paradise <b>September 2019</b></h3><p>September showcases the very best of our island conservation. The island has a long history of sustainability and care, earning national awards for protecting its unique biodiversity and reefs.</p></div>
  </div>
  <div class="awards">Awards Logos&nbsp; Of All Partnering Agencies</div>
  <div class="partners">
    <span class="partner round" style="background:#8a6a2a"></span>
    <span class="partner" style="background:#3fa9c9"></span>
    <span class="partner" style="background:#2a8a5a"></span>
    <span class="partner" style="background:#d89a2a"></span>
    <span class="partner" style="background:#d8452a"></span>
    <span class="partner round" style="background:#c8202a"></span>
    <span class="partner" style="background:#1f5fae"></span>
    <span class="partner round" style="background:#c8202a"></span>
    <span class="partner" style="background:#6a9ac8"></span>
  </div>
  <div class="back-footer"></div>
</section>
</body>
</html>
```